The Online Growth Blueprint for Garden & Patio Building Crews

We need a book cover design that is for a book targeting landscape and outdoor living contractors that helps them grow their business using online marketing.

We run a business focused on this industry so you can see what we do: https://gardencrewpromo.com/

The title is: The Online Growth Blueprint for Garden & Patio Building Crews

The author is: Trent Halvorsen
Some drafts have been done however they're still looking basic and somewhat amateur, we're looking for something that will stand out.

Target Market(s)

Landscape, Hardscape and Outdoor Living Contractors and Business Owners

Industry/Entity Type

Online Marketing

Font styles to use
Serif
Sans Serif

Requirements
Must have
• The part of the title that should stand out the most is the text "Online Growth Blueprint".
Should not have
• The color red

```html
<!DOCTYPE html>
<html lang="en">
<head>
<meta charset="utf-8">
<title>The Online Growth Blueprint for Garden &amp; Patio Building Crews</title>
<link rel="stylesheet" href="https://fonts.googleapis.com/css2?family=Bebas+Neue&family=Montserrat:wght@600;800&display=swap">
<style>
  :root {
    --backdrop: #e9eaec;
    --paper: #ffffff;
    --navy: #063f5f;
    --teal: #0fae9b;
    --ink: #111111;
    --rule: #222222;
    --author: #ffffff;
  }
  * { margin: 0; padding: 0; box-sizing: border-box; }
  html, body {
    width: 1200px;
    height: 1200px;
    overflow: hidden;
    background: var(--backdrop);
  }
  .canvas {
    position: relative;
    width: 1200px;
    height: 1200px;
  }
  .book-cover {
    position: absolute;
    left: 200px;
    top: 0;
    width: 800px;
    height: 1200px;
    background: var(--paper);
    overflow: hidden;
  }
  .cover-photo {
    position: absolute;
    left: 0;
    top: 640px;
    width: 800px;
    height: 560px;
    background:
      linear-gradient(180deg, rgba(255,255,255,1) 0%, rgba(255,255,255,0) 14%),
      linear-gradient(180deg,
        #dfe9f1 0%,
        #b9c9d6 18%,
        #8d8a86 32%,
        #c9a26a 44%,
        #e7c688 52%,
        #4a5a63 60%,
        #2f8fa3 68%,
        #7c7e80 80%,
        #4b4542 92%,
        #3a3533 100%);
  }
  .title-block {
    position: absolute;
    left: 0;
    top: 0;
    width: 800px;
    text-align: center;
  }
  .ruled-word {
    position: absolute;
    left: 35px;
    width: 730px;
    display: flex;
    align-items: center;
    gap: 14px;
    font-family: "Montserrat", sans-serif;
    font-weight: 800;
    font-size: 40px;
    line-height: 1;
    color: var(--ink);
  }
  .ruled-word::before,
  .ruled-word::after {
    content: "";
    flex: 1;
    height: 2px;
    background: var(--rule);
  }
  .ruled-the { top: 36px; }
  .ruled-for { top: 308px; }
  .title-line {
    position: absolute;
    left: 0;
    width: 800px;
    font-family: "Bebas Neue", sans-serif;
    line-height: 1;
    text-align: center;
    white-space: nowrap;
  }
  .line-highlight-top { top: 68px; font-size: 122px; color: var(--navy); }
  .line-highlight-main { top: 152px; font-size: 182px; color: var(--navy); }
  .line-audience-a { top: 352px; font-size: 134px; color: var(--teal); }
  .line-audience-b { top: 466px; font-size: 134px; color: var(--teal); }
  .line-audience-c { top: 580px; font-size: 134px; color: var(--navy); }
  .author-band {
    position: absolute;
    left: 0;
    bottom: 0;
    width: 800px;
    height: 78px;
    background: linear-gradient(180deg, rgba(40,36,34,0.35), rgba(40,36,34,0.6));
  }
  .author-name {
    position: absolute;
    left: 0;
    bottom: 18px;
    width: 800px;
    text-align: center;
    font-family: "Montserrat", sans-serif;
    font-weight: 600;
    font-size: 34px;
    letter-spacing: 0.32em;
    color: var(--author);
    line-height: 1;
  }
</style>
</head>
<body>
  <div class="canvas">
    <section class="book-cover">
      <div class="cover-photo" role="img" aria-label="Photo of a modern home at dusk with a lit patio, outdoor dining set, swimming pool, lounge chairs and a fire pit"></div>
      <div class="author-band"></div>

      <h1 class="title-block">
        <span class="ruled-word ruled-the">THE</span>
        <span class="title-line line-highlight-top">ONLINE GROWTH</span>
        <span class="title-line line-highlight-main">BLUEPRINT</span>
        <span class="ruled-word ruled-for">FOR</span>
        <span class="title-line line-audience-a">GARDEN &amp;</span>
        <span class="title-line line-audience-b">PATIO BUILDING</span>
        <span class="title-line line-audience-c">CREWS</span>
      </h1>

      <p class="author-name">TRENT HALVORSEN</p>
    </section>
  </div>
</body>
</html>
```